Website Tivnel

We are creating a new site for the company www.tivnel.com.br
We need a new design for the home and internal pages to go with it.
Our references style design:
http://www.quarbeckhub.com/
http://www.zolvimcentres.com/
http://www.pelmaridesk.com/
Site structure is in the attached documents.
background in white

Structure:
​1. Home
2. Empresa
3. Entenda o conceito
(dropdown) Salas Virtuais
(dropdown) Salas Prontas
4. Planos Virtuais
5. Salas Prontas
6. Contato

Benchmark:
www.fuvan.com.br
www.kjoffices.com.br
www.t4offices.com.br
www.lumeroffice.com.br
www.trevaloffice.com.br

Old site: http://www.tivnel.com.br/
Use the same footer information on the new site.

Target Market(s)

The site is on the rental of meeting rooms. These rooms contain furniture appropriate or can be rented for "virtual office".

Industry/Entity Type

It Company

Font styles to use
Sans Serif

Colors
3276b5
33a6d7
333333

Requirements
Must have
• Follow the colors of the logo
white background
horizontal menu
logo in the upper left corner
rotating banner
clean design
Should not have
• dark background
heavy colors
much information

```html
<!DOCTYPE html>
<html lang="pt">
<head>
<meta charset="utf-8">
<title>Tivnel – Escritórios Prontos</title>
<link href="https://fonts.googleapis.com/css2?family=Open+Sans:wght@400;600;700&family=PT+Sans:wght@400;700&family=Antonio:wght@400&display=swap" rel="stylesheet">
<style>
:root{
  --brand:#3276b5;
  --sky:#33a6d7;
  --ink:#333333;
  --muted:#8a8a8a;
  --line:#ececec;
  --white:#ffffff;
  --night:#1b1b1b;
}
*{box-sizing:border-box;margin:0;padding:0}
html,body{width:794px;height:1200px;overflow:hidden}
body{position:relative;background:var(--white);font-family:"Open Sans",sans-serif;color:var(--ink)}
.abs{position:absolute}
.brand{left:114px;top:16px;display:flex;align-items:center;gap:8px}
.brand-dot{width:22px;height:22px;border-radius:50%;background:var(--sky)}
.brand-name{font-family:"PT Sans",sans-serif;font-weight:700;font-size:28px;color:var(--brand)}
.social{right:113px;top:27px;display:flex;gap:4px}
.social span{width:17px;height:17px;border-radius:50%;background:var(--brand)}
.social span:last-child{background:#c9302c}
.tollfree{left:404px;top:62px;font-family:"PT Sans",sans-serif;font-size:14px;color:var(--brand)}
.search{left:571px;top:59px;width:110px;height:22px;border:1px solid #e2e2e2;font-size:7px;color:#999;padding:6px 8px;display:flex;justify-content:space-between;align-items:center}
.band{left:0;top:143px;width:794px;height:301px;background:linear-gradient(180deg,#3aa9dc,var(--sky))}
.nav{left:114px;top:104px;width:567px;height:40px;background:var(--ink);border-radius:3px 3px 0 0;display:flex;font-family:"PT Sans",sans-serif;font-size:11px;color:#fff}
.nav a{display:flex;align-items:center;padding:0 18px;height:100%;border-right:1px solid #454545;color:#fff;text-decoration:none}
.nav a:last-child{border:none}
.dropdown{left:278px;top:145px;width:126px;background:#fff;font-size:7.5px;z-index:3;box-shadow:0 1px 3px rgba(0,0,0,.15)}
.dropdown div{padding:9px 11px}
.dropdown .on{background:#5788c4;color:#fff}
.slider{left:114px;top:157px;width:567px;height:268px;background:#fff;padding:4px}
.slide{width:100%;height:100%;background:linear-gradient(180deg,#6e6f6e 0%,#a9a9a6 55%,#d8d8d4 100%)}
.caption{left:489px;top:227px;width:157px;min-height:141px;background:rgba(40,40,40,.92);color:#fff;padding:11px 13px 12px}
.caption h2{font-family:"Antonio",sans-serif;font-weight:400;font-size:18px;line-height:1.4;text-transform:uppercase;white-space:nowrap}
.caption p{font-size:7px;line-height:1.8;margin-top:8px;text-align:justify}
.arrows{left:379px;top:413px;display:flex;gap:2px}
.arrows span{width:17px;height:17px;background:#e8e8e8;border-radius:2px}
.welcome-photo{left:114px;top:466px;width:182px;height:138px;background:linear-gradient(180deg,#4a4236,#6d6251 60%,#3f7a2c)}
.welcome{left:312px;top:460px;width:369px}
.welcome h1{font-weight:400;font-size:18px;color:#444}
.welcome h1 em{font-style:normal;color:var(--brand)}
.welcome p{font-size:7px;line-height:1.95;color:var(--muted);margin-top:7px}
.rule{left:114px;width:567px;height:1px;background:var(--line)}
.feature{top:645px;width:180px;height:165px;border:1px solid var(--line);box-shadow:0 4px 4px -3px rgba(0,0,0,.12)}
.feature h3{display:flex;align-items:center;gap:8px;height:36px;padding:0 12px;border-bottom:1px solid var(--line);font-weight:400;font-size:10px;color:var(--brand);text-transform:uppercase}
.feature ul{list-style:none;padding:10px 14px}
.feature li{font-size:7.5px;color:#777;line-height:18px;display:flex;align-items:center;gap:7px}
.feature li::before{content:"";width:5px;height:5px;border-radius:50%;background:var(--brand)}
.rooms-title{left:114px;top:845px;font-family:"PT Sans",sans-serif;font-size:19px;color:var(--brand)}
.room{top:881px;width:134px;height:118px}
.footer{left:0;top:1021px;width:794px;height:139px;background:var(--brand);color:#fff}
.footer h4{position:absolute;font-weight:400;font-size:9px;text-transform:uppercase}
.address{left:135px;top:45px;font-size:8px;line-height:1.6}
.toll{left:137px;top:106px;font-size:8px}
.map{left:283px;top:18px;width:206px;height:104px;background:linear-gradient(135deg,#e9ecdf,#cfe0d6 60%,#9fc3dc)}
.field{height:20px;background:#fff;font-size:7px;color:#555;padding:6px 8px}
.send{left:505px;top:95px;width:62px;height:21px;background:#000;color:#fff;font-size:7.5px;display:flex;align-items:center;justify-content:center}
.bottom{left:0;top:1160px;width:794px;height:40px;background:var(--night)}
.copy{left:115px;top:16px;font-size:7px;color:#bbb}
.bottom-social{left:618px;top:10px;display:flex;gap:5px}
.bottom-social span{width:18px;height:18px;border:1px solid #555;border-radius:50%}
</style>
</head>
<body>
<div class="abs brand"><span class="brand-dot"></span><span class="brand-name">Tivnel</span></div>
<div class="abs social"><span></span><span></span><span></span></div>
<div class="abs tollfree">Toll Free : +051 4000-1234</div>
<div class="abs search">Search
  <svg width="8" height="8" viewBox="0 0 10 10"><circle cx="4" cy="4" r="3" fill="none" stroke="#999" stroke-width="1.2"/><path d="M6.3 6.3 9 9" stroke="#999" stroke-width="1.2"/></svg>
</div>

<div class="abs band"></div>
<nav class="abs nav">
  <a>Home</a><a>Empresa</a>
  <a>Entenda o conceito&nbsp;<svg width="7" height="5" viewBox="0 0 7 5"><path d="M1 1l2.5 2.5L6 1" fill="none" stroke="#fff"/></svg></a>
  <a>Planos Virtuais</a><a>Salas Prontas</a><a>Contato</a>
</nav>
<div class="abs dropdown"><div class="on">Salas Virtuais</div><div>Salas Prontas</div></div>

<div class="abs slider"><div class="slide" role="img" aria-label="Photo of a bright office lobby with black armchairs and potted trees"></div></div>
<div class="abs caption">
  <h2>Office solutions in<br>ready and virtual</h2>
  <p>Lorem ipsum dolor sit amet, consectetur adipiscing elit, sed do eiusmod tempor incididunt ut labore et dolore magna aliqua. Ut enim ad minim veniam,</p>
</div>
<div class="abs arrows"><span></span><span></span></div>

<div class="abs welcome-photo" role="img" aria-label="Photo of the office building entrance with a sculpture on the lawn"></div>
<section class="abs welcome">
  <h1>Welcome To <em>Tivnel</em></h1>
  <p>Lorem ipsum dolor sit amet, consectetur adipisc ng elit. Proin ultricies vestibulum velit, bibendum condimentum metus faucibus sed. Lorem ipsum dolor sit amet, consectetur adipisc ng elit. Proin ultricies vestibulum velit, bibendum condimentum metus faucibus sed. Lorem ipsum dolor sit amet, consectetur adipisc ng elit. Proin ultricies vestibulum velit, bibendum condimentum metus faucibus sed. Lorem ipsum dolor sit amet, consectetur adipisc ng elit. Proin ultricies vestibulum velit, bibendum condimentum metus faucibus sed.</p>
  <p>Lorem ipsum dolor sit amet, consectetur adipisc ng elit. Proin ultricies vestibulum velit, bibendum condimentum metus faucibus sed. Lorem ipsum dolor sit amet, consectetur adipisc ng elit. Proin ultricies vestibulum velit, bibendum condimentum metus faucibus sed. Lorem ipsum dolor sit amet, consectetur</p>
</section>
<div class="abs rule" style="top:624px"></div>

<div class="abs feature" style="left:114px">
  <h3><svg width="10" height="14" viewBox="0 0 10 14"><path d="M5 0a5 5 0 0 0-5 5c0 4 5 9 5 9s5-5 5-9a5 5 0 0 0-5-5z" fill="#3276b5"/><circle cx="5" cy="5" r="2" fill="#fff"/></svg>Privileged Location</h3>
  <ul><li>Upscale neighborhood</li><li>Only 5 minutes from the airport</li><li>Parking in the building</li><li>24h security</li><li>Close to great hotels and restaurants</li><li>Exceptional urban mobility</li></ul>
</div>
<div class="abs feature" style="left:312px">
  <h3><svg width="12" height="10" viewBox="0 0 12 10"><rect x=".5" y=".5" width="11" height="7" fill="none" stroke="#3276b5"/><path d="M3 9.5h6" stroke="#3276b5"/></svg>Exclusive Environment</h3>
  <ul><li>Building 1 per floor</li><li>All rooms with outside view</li><li>Furnished and equipped rooms</li><li>Differentiated Climate</li><li>Close to great hotels and restaurants</li><li>Exceptional urban mobility</li></ul>
</div>
<div class="abs feature" style="left:502px">
  <h3><svg width="14" height="14" viewBox="0 0 14 14"><circle cx="7" cy="7" r="4.5" fill="none" stroke="#3276b5" stroke-width="2.5" stroke-dasharray="2 1.5"/><circle cx="7" cy="7" r="1.5" fill="#3276b5"/></svg>Personalized Service</h3>
  <ul><li>Executive secretaries</li><li>Cutting Edge Technology</li><li>Power generator that meets all rooms</li><li>Redundancy in internet connectivity</li><li>that ensures high user</li><li>Exceptional urban mobility</li></ul>
</div>
<div class="abs rule" style="top:834px"></div>

<h2 class="abs rooms-title">Salas Prontas</h2>
<div class="abs room" style="left:114px;background:linear-gradient(180deg,#5b5d60,#7a7b7c)" role="img" aria-label="Photo of a meeting room with a round table"></div>
<svg class="abs" style="left:167px;top:927px" width="28" height="28" viewBox="0 0 28 28"><circle cx="14" cy="14" r="13" fill="none" stroke="#fff" stroke-width="1.5"/><circle cx="13" cy="13" r="4.5" fill="none" stroke="#fff" stroke-width="1.5"/><path d="M16.5 16.5l3.5 3.5" stroke="#fff" stroke-width="1.5"/></svg>
<div class="abs room" style="left:258px;background:linear-gradient(180deg,#2e2a24,#cbbfa6 60%,#e8e2d4)" role="img" aria-label="Photo of a small office with a desk and chairs"></div>
<div class="abs room" style="left:403px;background:linear-gradient(180deg,#6f7171,#bfc0bd 60%,#e4e4e0)" role="img" aria-label="Photo of the lobby with armchairs and trees"></div>
<div class="abs room" style="left:548px;background:linear-gradient(180deg,#5b5b58,#a7a49c 60%,#e6e6e3)" role="img" aria-label="Photo of a boardroom with a wall screen"></div>

<footer class="abs footer">
  <h4 style="left:114px;top:26px">Get in touch</h4>
  <svg class="abs" style="left:115px;top:46px" width="12" height="18" viewBox="0 0 10 14"><path d="M5 0a5 5 0 0 0-5 5c0 4 5 9 5 9s5-5 5-9a5 5 0 0 0-5-5z" fill="#fff"/><circle cx="5" cy="5" r="2" fill="#3276b5"/></svg>
  <div class="abs address">Unit Rio Grande do Sul - Porto Alegre<br>Rua das Acácias, 820 - 4th floor<br>Building Aurora Tower - Vila Clara -<br>Porto Alegre - RS</div>
  <div class="abs toll">Toll free:&nbsp;&nbsp;051 3000-5678</div>
  <div class="abs map" role="img" aria-label="Map showing the office location"></div>
  <h4 style="left:505px;top:17px">Get in touch</h4>
  <div class="abs field" style="left:505px;top:37px;width:84px">Name</div>
  <div class="abs field" style="left:597px;top:37px;width:84px">E - Mail</div>
  <div class="abs field" style="left:505px;top:65px;width:84px">Phone</div>
  <div class="abs field" style="left:597px;top:65px;width:84px">Message</div>
  <div class="abs send">Send</div>
</footer>
<div class="abs bottom">
  <div class="abs copy">Copyright © 2014 Tivnel. All rights reserved.</div>
  <div class="abs bottom-social"><span></span><span></span><span></span></div>
</div>
</body>
</html>
```